THE TALL COPPER ATLAS OF PORTS

subtitle: AN INTRO TO SEARCH ENGINE OPTIMIZATION
background: white
dimensions: 1562x2500

Target Market(s)

Marketing professionals

Industry/Entity Type

Digital Marketing

Font styles to use
Sans Serif

Colors
ffffff
1b1b1b
3176b5

Requirements
Should not have
• Images or graphics

```html
<!DOCTYPE html>
<html lang="en">
<head>
<meta charset="utf-8">
<title>The Tall Copper Atlas of Ports – Cover</title>
<link rel="stylesheet" href="https://fonts.googleapis.com/css2?family=Saira+Condensed:wght@600;700;800&display=swap">
<style>
  :root {
    --paper: #ffffff;
    --paper-shade: #d6d6d6;
    --ink: #1b1b1b;
    --accent: #1a93c9;
    --accent-deep: #0b5a7d;
    --accent-light: #3cb0d6;
    --tear-shadow: #4a4a4a;
  }
  html, body {
    margin: 0;
    padding: 0;
    width: 801px;
    height: 1200px;
    overflow: hidden;
    background: var(--paper);
  }
  .cover {
    display: block;
    width: 801px;
    height: 1200px;
  }
  .cover-text {
    font-family: "Saira Condensed", "Arial Narrow", sans-serif;
    font-weight: 700;
    fill: var(--ink);
  }
  .title-line { font-size: 118px; }
  .title-key { font-size: 470px; font-weight: 800; }
  .subtitle-small { font-size: 56px; }
  .subtitle-large { font-size: 126px; }
  .author-name { font-size: 104px; fill: var(--paper); font-weight: 600; }
  .author-band { fill: var(--accent); }
</style>
</head>
<body>
<svg class="cover" viewBox="0 0 801 1200" xmlns="http://www.w3.org/2000/svg" aria-label="Book cover: The Tall Copper Atlas of Ports">
  <defs>
    <radialGradient id="paperGlow" cx="0.48" cy="0.5" r="0.75">
      <stop offset="0" stop-color="var(--paper)"/>
      <stop offset="0.55" stop-color="#f1f1f1"/>
      <stop offset="1" stop-color="var(--paper-shade)"/>
    </radialGradient>
    <linearGradient id="spineShade" x1="0" x2="1" y1="0" y2="0">
      <stop offset="0" stop-color="#e2e2e2"/>
      <stop offset="0.55" stop-color="#bdbdbd"/>
      <stop offset="0.8" stop-color="#9a9a9a" stop-opacity="0.6"/>
      <stop offset="1" stop-color="#ffffff" stop-opacity="0"/>
    </linearGradient>
    <radialGradient id="keyFill" cx="0.5" cy="0.45" r="0.7">
      <stop offset="0" stop-color="var(--accent-light)"/>
      <stop offset="0.6" stop-color="#1f8db8"/>
      <stop offset="1" stop-color="var(--accent-deep)"/>
    </radialGradient>
  </defs>

  <!-- cover paper -->
  <rect class="cover-paper" width="801" height="1200" fill="url(#paperGlow)"/>

  <!-- spine crease -->
  <rect class="cover-spine" x="0" y="0" width="26" height="1200" fill="url(#spineShade)"/>

  <!-- title -->
  <text class="cover-text title-line" x="371" y="135" text-anchor="middle" textLength="300" lengthAdjust="spacingAndGlyphs">THE TALL</text>
  <text class="cover-text title-line" x="371" y="238" text-anchor="middle" textLength="513" lengthAdjust="spacingAndGlyphs">COPPER ATLAS OF</text>
  <text class="cover-text title-key" x="372" y="600" text-anchor="middle" textLength="520" lengthAdjust="spacingAndGlyphs" fill="url(#keyFill)">PORTS</text>

  <!-- slanted subtitle + author block -->
  <g class="subtitle-block" transform="translate(112 0) skewY(-12)">
    <text class="cover-text subtitle-small" x="0" y="798" textLength="508" lengthAdjust="spacingAndGlyphs">AN INTRO TO SEARCH ENGINE</text>
    <text class="cover-text subtitle-large" x="0" y="900" textLength="526" lengthAdjust="spacingAndGlyphs">OPTIMIZATION</text>
    <rect class="author-band" x="0" y="935" width="526" height="118"/>
    <text class="cover-text author-name" x="52" y="1018" textLength="420" lengthAdjust="spacingAndGlyphs">AUTHOR NAME</text>
  </g>

  <!-- torn paper edge -->
  <g class="torn-edge">
    <path fill="var(--tear-shadow)" opacity="0.75"
      d="M0 1112 L40 1106 L70 1114 L110 1104 L150 1112 L190 1102 L230 1110 L270 1100 L300 1110 L340 1102 L380 1112 L420 1100 L460 1108 L500 1098 L540 1108 L580 1100 L620 1110 L660 1102 L700 1110 L740 1100 L780 1108 L801 1104 L801 1132 L0 1132 Z"/>
    <path fill="var(--paper)"
      d="M0 1094 L20 1088 L45 1096 L70 1084 L95 1092 L130 1082 L160 1090 L200 1080 L230 1089 L265 1078 L300 1088 L330 1080 L365 1090 L400 1076 L440 1088 L470 1080 L505 1086 L540 1074 L575 1086 L610 1078 L645 1088 L680 1076 L715 1086 L750 1078 L780 1088 L801 1082 L801 1110 L770 1104 L740 1112 L700 1104 L660 1112 L620 1102 L580 1110 L540 1100 L500 1110 L460 1102 L420 1112 L380 1104 L340 1112 L300 1104 L260 1112 L220 1104 L180 1114 L140 1106 L100 1114 L60 1106 L20 1114 L0 1108 Z"/>
    <rect class="torn-page" x="0" y="1130" width="801" height="70" fill="var(--paper)"/>
  </g>
</svg>
</body>
</html>
```